Business Card Design

Velora Pixel Outreach

An online marketing consulting & strategy business for the cosmetic niche

We specialise in Increasing Leads, Conversions & Content Marketing

I am looking for a very clean, BOLD business card that is simple & effective

Target Market(s)

cosmetic surgeons & cosmetic clinics

Industry/Entity Type

Marketing

Contact Information for Business Card

Brett Kaminski
Online Marketing Strategist

Brett@VeloraPixelOutreach.example
0491 268 530

ProNet: in/brettkaminski

```html
<!DOCTYPE html>
<html lang="en">
<head>
<meta charset="utf-8">
<title>Brett Kaminski – Business Card</title>
<link href="https://fonts.googleapis.com/css2?family=Arimo:wght@400&display=swap" rel="stylesheet">
<style>
  :root {
    --card-bg: #ffffff;
    --ink: #1b1b1b;
    --band-start: #ffffff;
    --band-aqua: #4fe6de;
    --band-mint: #52f08e;
    --band-lime: #9cf21c;
  }
  html, body {
    margin: 0;
    padding: 0;
    overflow: hidden;
    background: var(--card-bg);
  }
  .card {
    position: relative;
    width: 1200px;
    height: 741px;
    background: var(--card-bg);
    font-family: "Arimo", Arial, sans-serif;
    font-weight: 400;
    color: var(--ink);
    overflow: hidden;
  }
  .line {
    position: absolute;
    margin: 0;
    font-size: 37px;
    line-height: 1;
    white-space: nowrap;
    letter-spacing: -0.2px;
  }
  .person-name  { left: 147px; top: 266px; }
  .person-role  { left: 147px; top: 315px; }
  .person-email { left: 147px; top: 364px; }

  .accent-band {
    position: absolute;
    left: 0;
    top: 434px;
    width: 1200px;
    height: 59px;
    background: linear-gradient(90deg,
      var(--band-start) 0%,
      var(--band-aqua) 33%,
      var(--band-mint) 55%,
      var(--band-lime) 100%);
  }

  .social-name  { left: 149px; top: 522px; font-size: 34px; }
  .social-handle { left: 316px; top: 522px; }

  .phone-icon {
    position: absolute;
    left: 695px;
    top: 517px;
    width: 47px;
    height: 47px;
  }
  .phone-number { left: 765px; top: 522px; font-size: 37px; }
</style>
</head>
<body>
  <div class="card">
    <p class="line person-name">Brett Kaminski</p>
    <p class="line person-role">Online Marketing Strategist</p>
    <p class="line person-email">Brett@VeloraPixelOutreach.example</p>

    <div class="accent-band"></div>

    <p class="line social-name">ProNet</p>
    <p class="line social-handle">in/brettkaminski</p>

    <svg class="phone-icon" viewBox="0 0 48 48" aria-hidden="true">
      <circle cx="24" cy="24" r="21.5" fill="none" stroke="#1b1b1b" stroke-width="3"/>
      <path d="M16.5 12.5c1.2-.9 2.5-.6 3.2.5l2.3 3.9c.6 1 .3 2.2-.6 2.9l-1.6 1.2c1 2.9 3.2 5.6 6 7.2l1.4-1.4c.8-.8 2.1-.9 3-.2l3.6 2.6c1 .8 1.2 2.1.3 3.2l-1.5 1.9c-1.4 1.6-3.8 2-6.2 1-6.2-2.8-10.8-8.1-12.6-14.6-.6-2.3.1-4.6 1.7-5.9z" fill="none" stroke="#1b1b1b" stroke-width="2.4" stroke-linejoin="round"/>
      <path d="M27 13.5a8 8 0 0 1 7.5 7.5M27 17.8a3.8 3.8 0 0 1 3.3 3.3" fill="none" stroke="#1b1b1b" stroke-width="2.2" stroke-linecap="round"/>
    </svg>
    <p class="line phone-number">0491 268 530</p>
  </div>
</body>
</html>
```